Tri Fold Brochure, Large Postcard, Letter head & Envelope For Real Estate Broker.
Cohesive Marketing Materials for Real Estate Broker in Rhode Island.
Thank You Creative!
Hi,
I have add Harlow Pennington logo in footer in my both design options please have a look.
Thanks.
Rewrote this section:
{HEADLINE} Native Son...
Being a committed community member, husband and devoted father are three key focal points in his world. In fact, his daughter Molly is a never-ending source of inspiration and happiness. Whether spending a day on Gull Island with wife Lorraine and Moll, or taking Molly to play golf, Tom cherishes those special moments spent with family.
Text for Brochure:
{HEADLINE} The Fine Art of Representing You...
Tom has been privileged to represent the owners of a diverse range of homes from waterfront showpieces to cozy Cape Cod's and everything in between.
Tom regards you and your property with the highest priority and respect and he guarantee's everything he does with the "Golden Rule" promise.
"I will be your trusted advisor navigating your home purchase and/or home sale for you as your advocate. If for any reason you are unsatisfied with my representation you are free to fire me, no catch's & no small print".
Our clients love what we do and we are confident you will as well. Our goal is to become YOUR Realtor and the only Realtor you want to refer to your family and friends. Put us to the Test!
{HEADLINE} There's a Saying: Conceive It, Believe It, Achieve It!
Just spend a day with Tom Ashby and you will see a perfect example of the power of attitude. This upbeat, native Rhode Islander approaches everything in life with an enthusiasm that is quite infectious. But where does Tom Ashby draw so much energy from—what makes him tick?
Being a committed community member and devoted father to his daughter Molly are two key focal points in his world. In fact, his daughter Molly is a never-ending source of inspiration and happiness. Whether spending a day on Gull Island, or taking Molly to play golf, Tom cherishes those special moments spent with her.
{HEADLINE} Children Bring a New Perspective on Life...
“Having a child rejuvenates you,” Tom says. “Things take on a fresh new perspective. It’s a joy to see the world through Molly’s eyes. Even the simplest things I used to take for granted now become exciting again because I can experience them with Moll.”
{HEADLINE} The Dreams and Aspirations of a Great Place, A Great People...
A native of Rhode Island, After graduating from East Marlow High School at the age of 17, Tom left his idyllic hometown of Pelton to serve with the Coastal Defense Volunteer Corps. Tom has proved that the old adage "You Cant Go Home Again" doesn't apply. After years away with the Marines and then building a large Real Estate practice in Southern Virginia, Tom and his family have come home to Rhode Island where it all started.
Tom wouldn’t dream of raising his daughter anywhere else. Surrounded by family, He believes there’s a quality of life here that begins with the ideals of its great people. “Rhode Island never changes in my view, we are a community of diverse backgrounds and cultures forged by the ocean and the coast and our rich history". "Our values, dreams and aspirations just seem to be the same , true and solid goals that our parents and grandparents strived for,” Tom explains. For Rhode Island residents one of the top goals seems to be the American Dream of home ownership. And that’s an area where Tom has become quite an authority—his other passion is his career as a real estate professional. In fact, this very passion has driven him to the top of his field. His nationally renowned performance is the direct result of his extensive knowledge and expertise backed by an unwavering commitment to go the distance for each client.
{HEADLINE} From Chubby Kid to Wrestling Champ...
But Tom will be the first to tell you that passion alone won’t guarantee success. Tom is a true believer in—and a perfect example of—the Yankee hard work ethic. Growing up as a overweight kid things weren’t handed to Tom, he had to struggle for most accomplishments. As a teen, Tom had a small dream to be the top wrestler in the area. He knew desire alone wasn't enough so he sought out the best wrestlers in the country to learn what they did to be so successful. Tom worked everyday to become just like the wrestlers he aspired to. His hard work and intense training paid off and Tmo went on to be a All State wrestler at East Marlow High School and a All New England and All American wrestler representing the state of Rhode Island at the Youth Union Grapple Series in Iowa.
Tom went on to represent the Coastal Defense Volunteer Corps in Greco Roman wrestling cumulating his wrestling career by winning the Service Branch Grapple Finals beating the formally unbeaten All Fleet heavyweight in the finals. Tom attributes his success on the mat to hard work, persistence and the techniques he learned from those who had gone before him.
{HEADLINE} Meet Tom, The Agent People love to Refer!
The road to becoming a top homeseller was not an easy one for Tom, either. From day one, Tom immersed himself with his typical zeal, taking every real estate class he could find, reading every book on the subject he could get his hands on, and spending hours studying with some of the top agents in the country.
{HEADLINE} Mastering His Craft: Day-To-Day Victories...
But true to form, Tom’s hard work eventually paid off. He started doing innovative personal marketing and set up systems to ensure outstanding service. Soon Tom was breaking records with his phenomenal performance. Tom is flattered by the requests he receives from companies and agents to share some of the secrets to his success. But to Tom, the status and accolades he’s earned in his profession aren’t as rewarding as the satisfying feeling he gets when he helps families achieve their dreams. “I work hard to master my craft,” Tom states, “Because so much is at stake when my clients have to sell an important part of their world. I want each of my clients to be confident of two things: they are working with the best and that I will do everything within my power to help them become successful.”
{HEADLINE} Reach Your Dreams With Tom Ashby By Your Side...
It makes perfect sense: you need to buy or sell your home, you want to be as successful as you can possibly be. That’s why you should work with Tom Ashby. Spend a few moments talking with Tom and see for yourself just how much he loves his work, and more importantly, how much of a difference this enthusiasm can make in your pursuit of the American Dream in the Ocean State...
{HEADLINE} In Conclusion...
Never losing sight of what is most important to our clients success, the fact that the majority of business is based on referrals from satisfied clients is a telling sign that Toms style of service is anything but standard. He often builds long tern relationships with his clients and becomes a trusted advisor and a friend. Whether buying or selling, Tom has the market knowledge, business savvy, care and dedication to help you make the most of your real estate opportunities.
I am working on the text for the brochure but most likely it will come after I pick the winning the design to be inserted after award.

```html
<!DOCTYPE html>
<html lang="en">
<head>
<meta charset="utf-8">
<title>Tom Ashby – Marketing Suite</title>
<link rel="stylesheet" href="https://fonts.googleapis.com/css2?family=Cormorant+Garamond:wght@500;600&family=Open+Sans:wght@400;600;700&display=swap">
<style>
  :root{
    --crimson:#c5123a;
    --crimson-dark:#a80f31;
    --gold:#a8875a;
    --paper:#ffffff;
    --backdrop:#efefef;
    --ink:#3a3a3a;
    --muted:#8a8a8a;
    --sky:#b9cfe3;
    --sea:#6f95a8;
    --grass:#7d9460;
    --stone:#9b8f80;
    --wood:#8a4b2a;
    --frame-blue:#d6e6f2;
  }
  *{box-sizing:border-box;margin:0;padding:0}
  html,body{width:1200px;height:595px;overflow:hidden;background:var(--backdrop);font-family:"Open Sans",sans-serif;color:var(--ink)}
  .canvas{position:relative;width:1200px;height:595px}
  .piece{position:absolute;background:var(--paper);box-shadow:0 1px 3px rgba(0,0,0,.18)}
  .photo{position:absolute}
  .wordmark{font-family:"Cormorant Garamond",serif;font-weight:600;color:var(--gold);letter-spacing:2px;text-align:center;line-height:1}

  /* envelope */
  .envelope{left:20px;top:25px;width:298px;height:165px;background:none;box-shadow:none}
  .envelope svg{position:absolute;left:0;top:0}
  .envelope .return{position:absolute;left:0;width:298px;top:44px;text-align:center;font-size:4px;color:var(--muted)}
  .envelope .wordmark{position:absolute;left:0;width:298px;top:74px;font-size:16px}
  .envelope .window{position:absolute;left:22px;top:116px;width:78px;height:26px;border:1px solid #d7d7d7;background:#fafafa}
  .envelope .band{position:absolute;left:0;bottom:0;width:298px;height:16px;background:var(--crimson)}

  /* postcards */
  .postcard-front{left:20px;top:198px;width:298px;height:92px;overflow:hidden}
  .postcard-back{left:20px;top:297px;width:298px;height:92px;background:var(--frame-blue);padding:5px}
  .postcard-back .inner{position:relative;width:100%;height:100%;background:var(--paper)}
  .postcard-back .rule{position:absolute;left:14px;right:14px;height:1px;background:#c9d8e4}
  .postcard-back .agent{position:absolute;left:8px;bottom:6px;width:14px;height:16px;background:#5d6470}
  .postcard-back .sig{position:absolute;left:26px;bottom:8px;font-size:4.5px;color:var(--muted)}

  /* letterhead */
  .letterhead{left:333px;top:20px;width:245px;height:553px}
  .letterhead .wordmark{position:absolute;left:0;width:245px;top:40px;font-size:17px}
  .letterhead .band{position:absolute;left:0;width:245px;bottom:18px;height:11px;background:var(--crimson)}
  .letterhead .footer{position:absolute;left:0;width:245px;bottom:8px;text-align:center;font-size:3.6px;color:var(--muted)}

  /* brochure shared */
  .brochure{left:595px;width:585px;height:270px;overflow:hidden}
  .brochure-outside{top:20px}
  .brochure-inside{top:305px;height:268px}
  .panel{position:absolute;top:0;height:100%;width:195px;overflow:hidden}
  .panel-1{left:0}.panel-2{left:195px}.panel-3{left:390px}
  .crimson-block{position:absolute;background:var(--crimson);color:#fff}

  .outside-contact{font-size:4.5px;line-height:1.5;padding:6px}
  .outside-contact strong{display:block;font-size:6px;margin-bottom:2px}
  .cover-text{position:absolute;left:0;top:196px;width:195px;padding:0 14px;text-align:right}
  .cover-text .wordmark{text-align:right;font-size:13px;margin-top:14px}
  .cover-text p{font-size:4.5px;color:var(--muted);margin-top:5px}
  .panel-2 .wordmark{position:absolute;left:0;width:195px;top:136px;font-size:15px;color:#fff}

  /* inside */
  .inside-left{left:0;top:0;width:195px;height:268px}
  .inside-left h2{font-family:"Cormorant Garamond",serif;font-weight:600;font-size:15px;line-height:1;position:absolute;left:10px;top:12px;width:80px}
  .inside-left .copy{position:absolute;left:10px;top:52px;width:82px;font-size:4.4px;line-height:1.55}
  .inside-left .copy p+p{margin-top:5px}
  .feature{position:absolute;left:0;top:0;width:100%}
  .feature h3{font-size:6.5px;font-weight:700;color:var(--crimson);margin:0 0 2px}
  .feature p{font-size:4.4px;line-height:1.5;color:var(--ink)}
  .worth h3{font-size:6.5px;font-weight:700;margin-bottom:4px}
  .worth p{font-size:4.4px;line-height:1.55}
</style>
</head>
<body>
<main class="canvas">

  <!-- Envelope with open flap -->
  <section class="piece envelope" aria-label="Envelope">
    <svg width="298" height="165" viewBox="0 0 298 165">
      <rect x="0" y="22" width="298" height="143" fill="#ffffff" stroke="#dcdcdc"/>
      <path d="M0 22 L12 4 Q14 0 20 0 L278 0 Q284 0 286 4 L298 22 Z" fill="#f7f7f7" stroke="#dcdcdc"/>
    </svg>
    <p class="return">12 Harbor Lane · Pelton, RI</p>
    <p class="wordmark">TOM ASHBY</p>
    <div class="window"></div>
    <div class="band"></div>
  </section>

  <!-- Postcard front -->
  <section class="piece postcard-front">
    <div class="photo" role="img" aria-label="Shingled coastal house on a green lawn under a blue sky"
         style="inset:0;background:linear-gradient(180deg,var(--sky) 0%,#dbe6ef 45%,var(--stone) 62%,var(--grass) 75%,#5f7a45 100%)"></div>
  </section>

  <!-- Postcard back -->
  <section class="piece postcard-back">
    <div class="inner">
      <div class="rule" style="top:14px"></div>
      <div class="rule" style="top:26px"></div>
      <div class="rule" style="top:38px"></div>
      <div class="rule" style="top:50px"></div>
      <div class="rule" style="top:62px"></div>
      <div class="agent" role="img" aria-label="Portrait of the agent"></div>
      <p class="sig">Tom Ashby, Realtor · 401-555-0142</p>
    </div>
  </section>

  <!-- Letterhead -->
  <section class="piece letterhead">
    <p class="wordmark">TOM ASHBY</p>
    <div class="band"></div>
    <p class="footer">Tom Ashby · Harlow Pennington · 12 Harbor Lane, Pelton, RI 02852 · 401-555-0142 · tom@tidewaterhomes.com</p>
  </section>

  <!-- Brochure outside -->
  <section class="piece brochure brochure-outside">
    <div class="panel panel-1">
      <div class="photo" role="img" aria-label="Stone-walled estate on a green hillside" style="left:0;top:0;width:97px;height:70px;background:linear-gradient(180deg,#c7d8e6,#8fa473 55%,#6d8650)"></div>
      <div class="photo" role="img" aria-label="Large white house with pool" style="left:98px;top:0;width:97px;height:70px;background:linear-gradient(180deg,#a9c5de,#d8d3c8 50%,#7a9460)"></div>
      <div class="photo" role="img" aria-label="Shingled house with trees and lawn" style="left:0;top:71px;width:97px;height:64px;background:linear-gradient(180deg,#b8cde0,#8a8070 45%,#6f8a4f)"></div>
      <div class="crimson-block outside-contact" style="left:98px;top:71px;width:97px;height:64px">
        <strong>Tom Ashby</strong>Harlow Pennington<br>401-555-0142
      </div>
      <div class="photo" role="img" aria-label="Rocky ocean shoreline" style="left:0;top:136px;width:195px;height:134px;background:linear-gradient(180deg,#c6d8e8,#7fa3bb 40%,var(--sea) 60%,#7e7566 100%)"></div>
    </div>
    <div class="panel panel-2">
      <div class="photo" role="img" aria-label="Country house surrounded by gardens" style="left:1px;top:0;width:194px;height:110px;background:linear-gradient(180deg,#b4cbe0,#c9c1b2 45%,#7c9658)"></div>
      <div class="crimson-block" style="left:1px;top:110px;width:194px;height:70px"></div>
      <p class="wordmark">TOM ASHBY</p>
      <div class="photo" role="img" aria-label="Coastline with waves over rocks" style="left:1px;top:180px;width:194px;height:90px;background:linear-gradient(180deg,#cddde9,#88a9bf 45%,#6b8b9b 65%,#847a69)"></div>
    </div>
    <div class="panel panel-3">
      <div class="photo" role="img" aria-label="Grand shingled seaside house on a lawn" style="left:1px;top:0;width:194px;height:190px;background:linear-gradient(180deg,#a8c2da,#d2dce4 35%,#8f8576 55%,#7a9354 75%,#5e7843)"></div>
      <div class="cover-text">
        <p class="wordmark">TOM ASHBY</p>
        <p>The Fine Art of Representing You</p>
      </div>
    </div>
  </section>

  <!-- Brochure inside -->
  <section class="piece brochure brochure-inside">
    <div class="crimson-block inside-left">
      <h2>Real Estate Redefined</h2>
      <div class="copy">
        <p>Tom has been privileged to represent the owners of a diverse range of homes, from waterfront showpieces to cozy capes and everything in between.</p>
        <p>Tom regards you and your property with the highest priority and respect.</p>
        <p>Our clients love what we do and we are confident you will as well. Put us to the test!</p>
      </div>
      <div class="photo" role="img" aria-label="Portrait of the agent in a dark suit" style="left:100px;top:12px;width:86px;height:90px;background:linear-gradient(180deg,#9aa3ad,#3f4550)"></div>
    </div>

    <div class="panel panel-2">
      <div class="photo" role="img" aria-label="Warm wood-paneled interior room" style="left:4px;top:4px;width:187px;height:74px;background:linear-gradient(135deg,#c98a52,var(--wood) 55%,#4e2a18)"></div>
      <div class="feature" style="top:86px;padding:0 8px">
        <h3>Featured Property for Sale</h3>
        <p>Browse our newest waterfront and village listings online.</p>
      </div>
      <div class="photo" role="img" aria-label="Harbor view with boats" style="left:8px;top:112px;width:179px;height:56px;background:linear-gradient(180deg,#c6d8e8,#6f95a8 60%,#566f7d)"></div>
      <div class="feature" style="top:176px;padding:0 8px">
        <h3>Market Trends Newsletter</h3>
        <p>Monthly insight on prices and sales across the Ocean State.</p>
      </div>
      <div class="feature" style="top:210px;padding:0 8px">
        <h3>Email Listing Alerts</h3>
        <p>Get new homes that match your search sent to your inbox.</p>
      </div>
    </div>

    <div class="panel panel-3">
      <div class="crimson-block worth" style="left:0;top:0;width:195px;height:170px;padding:12px 10px">
        <h3>What's Your Home Worth</h3>
        <p>Curious what your property could sell for today? Request a free, no obligation market analysis from Tom.</p>
        <p style="margin-top:5px">Call 401-555-0142 to get started.</p>
      </div>
      <div class="photo" role="img" aria-label="Rocky coast meeting the sea" style="left:0;top:170px;width:195px;height:98px;background:linear-gradient(180deg,#c9dbea,#7fa2b9 45%,#5f8194 65%,#8a7f6c)"></div>
    </div>
  </section>

</main>
</body>
</html>
```